Willowmere Counseling (Endure - Mend - Flourish) - Double Sided Business Card

I would like a 2-sided business card. Front: Matte Black or Navy with Logo & Tagline. Back: Name, Address, Phone Number, Email, & Website (maybe would like to include a small map pin-pointing location); Prefer front to be a gold/silver foil (iridescent); Back prefer white or light colored background with lettering that is easy to read and simple

Target Market(s)

Individuals & Couples (13 y.o. - ALL Adults); High end clientele

Industry/Entity Type

Licensed Professional Counselor (Mental Health)

Contact Information for Business Card

Name: Willowmere Counseling; Tagline: Endure - Mend - Flourish; Address: 3870 N. Garrick Ave., Suite 214, Fort Worth, TX 76132; Phone: (214) 555-0187; Website: www.WillowmereCounseling.example

Font styles to use
Serif

Requirements
Must have
• Logo on Front (Large) prefer gold/silver foil on a matte dark color (i.e. black, navy, etc.); Back of Card: All other relevant information

```html
<!DOCTYPE html>
<html lang="en">
<head>
<meta charset="utf-8">
<title>Willowmere Counseling — Business Card</title>
<link href="https://fonts.googleapis.com/css2?family=Cinzel:wght@400;600;700&family=Arimo:wght@400&display=swap" rel="stylesheet">
<style>
  :root {
    --stage: #d9d9d9;
    --card-dark: #1b1b1b;
    --gold: #d4b95c;
    --gold-deep: #c9ab4c;
    --grey: #84878a;
    --grey-text: #4a4a4a;
    --white: #ffffff;
  }
  * { box-sizing: border-box; margin: 0; padding: 0; }
  html, body { width: 1200px; height: 901px; overflow: hidden; }
  body {
    background: var(--stage);
    display: flex; flex-direction: column; align-items: center; justify-content: center;
    gap: 48px;
    font-family: "Arimo", Arial, sans-serif;
  }
  .card {
    position: relative; width: 620px; height: 354px; overflow: hidden;
    box-shadow: 0 10px 24px rgba(0,0,0,.25);
  }

  /* Wordmark */
  .wordmark { text-align: center; font-family: "Cinzel", "Times New Roman", serif; }
  .wordmark-name {
    font-weight: 600; font-size: 32px; letter-spacing: 1px; line-height: 1.1;
    color: var(--gold);
  }
  .wordmark-name span { display: block; white-space: nowrap; }
  .wordmark-rule { height: 2px; margin: 10px 0 8px; background: var(--white); }
  .wordmark-tagline {
    font-size: 13px; letter-spacing: 1.5px; color: var(--gold); white-space: nowrap;
  }

  /* Front */
  .card-front { background: var(--card-dark); }
  .card-front .wordmark { position: absolute; right: 48px; top: 104px; width: 300px; }

  /* Back */
  .card-back { background: var(--white); }
  .card-back .band-grey { position: absolute; left: 0; right: 0; top: 196px; height: 132px; background: var(--grey); }
  .card-back .block-gold { position: absolute; left: 440px; right: 0; top: 112px; height: 112px; background: var(--gold); }
  .card-back .seal {
    position: absolute; left: 440px; top: 108px; width: 172px; height: 172px;
    border-radius: 50%; background: var(--white); border: 14px solid var(--grey);
    box-shadow: 0 0 0 8px var(--white);
  }
  .card-back .wordmark { position: absolute; right: 40px; top: 16px; width: 270px; }
  .card-back .wordmark-name { font-size: 24px; }
  .card-back .wordmark-rule { background: var(--grey); margin: 7px 0 5px; }
  .card-back .wordmark-tagline { font-size: 11px; }

  .person { position: absolute; left: 40px; top: 118px; }
  .person-name {
    font-family: "Cinzel", "Times New Roman", serif; font-weight: 700;
    font-size: 26px; color: var(--gold-deep); letter-spacing: .5px;
  }
  .person-title { font-size: 15px; color: var(--grey-text); margin-top: 2px; }

  .contact { position: absolute; left: 40px; top: 214px; list-style: none; color: var(--white); font-size: 14px; line-height: 1.3; }
  .contact li { display: flex; align-items: flex-start; gap: 9px; margin-bottom: 5px; }
  .contact li.gap-after { margin-bottom: 10px; }
  .contact svg { flex: none; width: 14px; height: 14px; margin-top: 2px; fill: var(--gold); }
</style>
</head>
<body>

  <section class="card card-front" aria-label="Card front">
    <div class="wordmark">
      <div class="wordmark-name"><span>Willowmere</span><span>Counseling</span></div>
      <div class="wordmark-rule"></div>
      <div class="wordmark-tagline">ENDURE - MEND - FLOURISH</div>
    </div>
  </section>

  <section class="card card-back" aria-label="Card back">
    <div class="band-grey"></div>
    <div class="block-gold"></div>
    <div class="seal"></div>

    <div class="wordmark">
      <div class="wordmark-name"><span>Willowmere</span><span>Counseling</span></div>
      <div class="wordmark-rule"></div>
      <div class="wordmark-tagline">ENDURE - MEND - FLOURISH</div>
    </div>

    <div class="person">
      <div class="person-name">DANIEL WHITCOMBE</div>
      <div class="person-title">CEO/Founder</div>
    </div>

    <ul class="contact">
      <li class="gap-after">
        <svg viewBox="0 0 14 14" aria-hidden="true"><path d="M7 0a5 5 0 0 0-5 5c0 3.6 5 9 5 9s5-5.4 5-9a5 5 0 0 0-5-5zm0 7a2 2 0 1 1 0-4 2 2 0 0 1 0 4z"/></svg>
        <span>3870 N. Garrick Ave., Suite 214,<br>Fort Worth, TX 76132</span>
      </li>
      <li>
        <svg viewBox="0 0 14 14" aria-hidden="true"><path d="M3 1l2.2 2.6-1.3 1.6a8 8 0 0 0 4.9 4.9l1.6-1.3L13 11l-1.4 2.2C6 13 1 8 .8 2.4z"/></svg>
        <span>(214) 555-0187</span>
      </li>
      <li>
        <svg viewBox="0 0 14 14" aria-hidden="true"><path d="M1 3h12v8H1zM1.6 3.4 7 8l5.4-4.6" stroke="#84878a" stroke-width="1"/></svg>
        <span>info@willowmerecounseling.example</span>
      </li>
      <li>
        <svg viewBox="0 0 14 14" aria-hidden="true"><circle cx="7" cy="7" r="6"/><path d="M1 7h12M7 1c-2.5 3-2.5 9 0 12M7 1c2.5 3 2.5 9 0 12" stroke="#84878a" stroke-width="1" fill="none"/></svg>
        <span>www.WillowmereCounseling.example</span>
      </li>
    </ul>
  </section>

</body>
</html>
```